Looking for a website design for my company
Services we offer:
Phone Repair
TV Mounting
Security Camera Installation
Networking / Wi-Fi
Smart Home Services
IT Support

Looking for a website similar to qarnel.com

Few tabs
About Us
Contact Us
Areas Served
Pricing and Services

```html
<!DOCTYPE html>
<html lang="en">
<head>
<meta charset="utf-8">
<title>Vanto Rim — Home Maintenance Made Easy</title>
<link href="https://fonts.googleapis.com/css2?family=Barlow+Semi+Condensed:wght@500;600;700&family=Poppins:wght@400;500;600&display=swap" rel="stylesheet">
<style>
  :root {
    --orange: #f7941d;
    --orange-soft: #fde3c4;
    --ink: #1f1f1f;
    --text: #7a7a7a;
    --grey-bg: #f3f3f3;
    --card: #ffffff;
    --btn-grey: #6c6c6c;
    --head: "Barlow Semi Condensed", sans-serif;
    --body: "Poppins", sans-serif;
  }
  * { margin: 0; padding: 0; box-sizing: border-box; }
  html, body { width: 1200px; height: 3846px; overflow: hidden; }
  body { position: relative; background: #fff; font-family: var(--body); color: var(--text); }
  .abs { position: absolute; }
  .btn {
    position: absolute; display: flex; align-items: center; justify-content: center;
    background: var(--orange); color: #fff; border-radius: 30px;
    font-family: var(--head); font-weight: 600; font-size: 15px; letter-spacing: .3px;
  }
  .section-title { position: absolute; font-family: var(--head); font-weight: 700; color: var(--ink); font-size: 29px; line-height: 34px; letter-spacing: .3px; }
  .centered { left: 0; width: 1200px; text-align: center; }
  .para { font-size: 11px; line-height: 19.5px; color: var(--text); }

  /* header */
  .hero-bg { left: 0; top: 0; width: 1200px; height: 620px; background: var(--grey-bg); }
  .logo { font-family: var(--head); font-weight: 700; font-size: 36px; line-height: 44px; color: var(--orange); }
  .nav { left: 413px; top: 32px; display: flex; gap: 25px; font-size: 12px; color: #555; }
  .nav .active { color: var(--orange); }
  .phone-btn { left: 885px; top: 21px; width: 154px; height: 40px; font-size: 14px; gap: 7px; }

  .hero-title { left: 163px; top: 186px; font-family: var(--head); font-weight: 700; font-size: 37px; line-height: 45px; color: var(--ink); }
  .hero-text { left: 163px; top: 274px; width: 320px; }
  .hero-btn { left: 161px; top: 333px; width: 154px; height: 40px; }
  .hero-art { left: 545px; top: 90px; width: 510px; height: 510px;
    background: radial-gradient(ellipse 55% 52% at 58% 52%, #f7941d 0%, #f8a440 30%, #f5cfa0 55%, rgba(243,243,243,0) 78%); }

  /* welcome */
  .welcome-blob-back { left: 161px; top: 687px; width: 414px; height: 350px; border-radius: 48% 52% 55% 45% / 50% 45% 55% 50%; background: var(--orange-soft); }
  .welcome-photo { left: 168px; top: 690px; width: 400px; height: 368px; border-radius: 55% 45% 42% 58% / 48% 52% 48% 52%;
    background: linear-gradient(160deg, #d9d9d9 0%, #9a9a9a 40%, #5a5a5a 60%, #efefef 100%); }
  .welcome-title { left: 631px; top: 745px; }
  .welcome-text { left: 631px; top: 791px; width: 400px; }
  .welcome-btn { left: 630px; top: 955px; width: 139px; height: 40px; }

  /* offer */
  .offer-bg { left: 0; top: 1218px; width: 1200px; height: 472px; background: var(--grey-bg); }
  .offer-art { left: 500px; top: 1105px; width: 200px; height: 145px;
    background: radial-gradient(ellipse 50% 50% at 50% 55%, #f7941d 0%, #f9ad55 35%, rgba(255,255,255,0) 72%); }
  .offer-title { top: 1285px; }
  .offer-sub { top: 1326px; }
  .service-card { position: absolute; top: 1403px; width: 126px; height: 142px; background: var(--card);
    display: flex; flex-direction: column; align-items: center; padding-top: 24px;
    font-family: var(--head); font-weight: 600; font-size: 13px; color: #555; text-align: center; line-height: 21px; }
  .service-card svg { width: 44px; height: 44px; margin-bottom: 8px; }
  .offer-btn { left: 522px; top: 1575px; width: 154px; height: 40px; }

  /* call to action */
  .cta-photo { left: 0; top: 1690px; width: 1200px; height: 450px;
    background: linear-gradient(90deg, #5c4b3c 0%, #a58a72 18%, #e4d9cf 34%, #efe9e2 52%, #c7bfb8 70%, #d9d9de 100%); }
  .cta-circle { left: 649px; top: 1726px; width: 374px; height: 374px; border-radius: 50%; background: var(--orange);
    display: flex; flex-direction: column; align-items: center; color: #fff; text-align: center; }
  .cta-logo { margin-top: 52px; font-family: var(--head); font-weight: 700; font-size: 27px; line-height: 32px; }
  .cta-title { margin-top: 8px; font-family: var(--head); font-weight: 700; font-size: 42px; line-height: 54px; }
  .cta-text { margin-top: 8px; font-size: 11px; line-height: 19px; }
  .cta-btn { position: static; margin-top: 14px; width: 154px; height: 40px; background: #fff; color: var(--ink); }

  /* testimonials */
  .testi-title { top: 2209px; }
  .testi { position: absolute; top: 2262px; width: 275px; }
  .testi .quote { font-family: Georgia, serif; font-size: 60px; line-height: 40px; color: var(--orange-soft); height: 26px; }
  .testi .person { display: flex; align-items: center; gap: 15px; margin-top: 18px; }
  .avatar { width: 54px; height: 54px; border-radius: 50%; background: linear-gradient(135deg, #d8b59a, #6d5646); }
  .client-name { font-family: var(--head); font-weight: 600; font-size: 12px; color: var(--orange); }
  .stars { color: var(--orange); font-size: 16px; letter-spacing: 1px; line-height: 20px; }

  /* pricing */
  .pricing-bg { left: 0; top: 2507px; width: 1200px; height: 508px; background: var(--grey-bg); }
  .pricing-title { top: 2573px; }
  .plan { position: absolute; width: 196px; background: #fff; border: 1px solid #e6e6e6; }
  .plan .price { height: 59px; border-bottom: 1px solid #e6e6e6; text-align: center; font-family: var(--head); font-weight: 600; color: #6c6c6c; font-size: 29px; padding-top: 12px; }
  .plan .price small { font-size: 16px; }
  .plan ul { list-style: none; padding: 22px 0 0 26px; }
  .plan li { font-size: 11px; height: 30px; color: var(--text); display: flex; align-items: flex-start; gap: 12px; }
  .plan li::before { content: ""; width: 6px; height: 6px; border-radius: 50%; background: var(--orange); margin-top: 5px; }
  .plan .select { position: relative; margin: 4px auto 0; width: 101px; height: 33px; background: var(--btn-grey); font-size: 14px; }
  .plan.featured { border-color: var(--orange); }
  .plan.featured .price { color: var(--orange); height: 77px; }
  .plan.featured .select { background: var(--orange); }
  .plan .monthly { display: block; font-family: var(--body); font-size: 10px; font-weight: 400; color: var(--orange); margin-top: 4px; }

  /* areas */
  .areas-art { left: 75px; top: 3085px; width: 480px; height: 460px;
    background: radial-gradient(ellipse 42% 48% at 48% 50%, #3a3a3a 0%, #8a8a8a 25%, #f1b46a 45%, #f4ede6 62%, rgba(255,255,255,0) 78%); }
  .areas-title { left: 631px; top: 3106px; }
  .area-item { position: absolute; display: flex; align-items: center; gap: 10px; font-size: 11px; color: var(--text); }
  .area-item svg { width: 14px; height: 18px; }
  .footer-wave { left: 0; top: 3390px; width: 1200px; height: 160px; }
  .family-photo { left: 630px; top: 3339px; width: 570px; height: 203px; border-radius: 110px 0 0 110px / 203px 0 0 0;
    background: linear-gradient(90deg, #3f444e 0%, #6d6a66 30%, #a99a88 60%, #cfc6bb 100%); }

  /* footer */
  .footer { left: 0; top: 3542px; width: 1200px; height: 304px; background: var(--orange); color: #fff; }
  .footer-logo { left: 0; width: 1200px; top: 3584px; text-align: center; font-family: var(--head); font-weight: 700; font-size: 40px; line-height: 48px; color: #fff; }
  .contact-box { left: 161px; top: 3646px; width: 876px; height: 96px; border: 1px solid rgba(255,255,255,.45); display: flex; color: #fff; }
  .contact-col { flex: 1; display: flex; align-items: center; gap: 18px; padding-left: 22px; border-right: 1px solid rgba(255,255,255,.45); }
  .contact-col:last-child { border-right: 0; }
  .contact-icon { width: 54px; height: 54px; border-radius: 50%; background: rgba(255,255,255,.25); display: flex; align-items: center; justify-content: center; }
  .contact-label { font-size: 10px; opacity: .85; text-transform: uppercase; }
  .contact-value { font-size: 11px; line-height: 18px; }
  .footer-links { left: 0; width: 1200px; top: 3768px; display: flex; justify-content: center; gap: 22px; font-size: 12px; color: #fff; }
  .copyright { left: 0; width: 1200px; top: 3800px; text-align: center; font-size: 10px; color: rgba(255,255,255,.85); }
</style>
</head>
<body>

<!-- Header & hero -->
<div class="abs hero-bg"></div>
<div class="abs hero-art" role="img" aria-label="Illustration of a man relaxing in an orange armchair controlling a smart home thermostat app on large phone screens"></div>
<svg class="abs" style="left:0;top:500px" width="1200" height="130" viewBox="0 0 1200 130" aria-hidden="true">
  <path d="M0 48 C 260 -10, 450 40, 620 80 C 820 128, 1030 100, 1200 55 L1200 130 L0 130 Z" fill="#fff"/>
</svg>

<div class="abs logo" style="left:161px;top:14px">Vanto Rim</div>
<nav class="abs nav">
  <span class="active">HOME</span><span>ABOUT US</span><span>SERVICES</span><span>PRICING</span><span>AREAS SERVED</span><span>CONTACT</span>
</nav>
<div class="btn phone-btn">
  <svg width="14" height="14" viewBox="0 0 24 24" aria-hidden="true"><path fill="#fff" d="M6.6 10.8a15 15 0 0 0 6.6 6.6l2.2-2.2c.3-.3.7-.4 1-.2 1.1.4 2.3.6 3.6.6.6 0 1 .4 1 1V20c0 .6-.4 1-1 1A17 17 0 0 1 3 4c0-.6.4-1 1-1h3.5c.6 0 1 .4 1 1 0 1.3.2 2.5.6 3.6.1.3 0 .7-.2 1z"/></svg>
  123 456 7890
</div>

<h1 class="abs hero-title">HOME MAINTENANCE<br>MADE EASY</h1>
<p class="abs para hero-text">Lorem Ipsum is simply dummy text of the printing and typesetting industry. Lorem Ipsum has been the industry</p>
<div class="btn hero-btn">BOOK SERVICES</div>

<!-- Welcome -->
<div class="abs welcome-blob-back"></div>
<div class="abs welcome-photo" role="img" aria-label="Photo of a modern living room with a wall-mounted TV and white furniture"></div>
<h2 class="section-title welcome-title">WELCOME TO VANTO RIM</h2>
<div class="abs para welcome-text">
  <p>Lorem Ipsum is simply dummy text of the printing and typesetting industry. Lorem Ipsum has been the industry's standard dummy text ever since the 1500s, when an unknown printer took a galley of type and scrambled it to make a type specimen book.</p>
  <p style="margin-top:19px">It has survived not only five centuries, but also the leap into electronic typesetting, remaining essentially unchanged.</p>
</div>
<div class="btn welcome-btn">READ MORE</div>

<!-- What we offer -->
<div class="abs offer-bg"></div>
<div class="abs offer-art" role="img" aria-label="Illustration of a woman in an orange sweater leaning over the section edge"></div>
<h2 class="section-title centered offer-title">WHAT WE OFFER</h2>
<p class="abs para centered offer-sub">Lorem Ipsum is simply dummy text of the printing and typesetting industry.<br>Lorem Ipsum has been the industry</p>

<div class="service-card" style="left:175px">
  <svg viewBox="0 0 44 44" fill="none" stroke="#f7941d" stroke-width="2"><rect x="14" y="4" width="16" height="34" rx="2"/><line x1="20" y1="33" x2="24" y2="33"/></svg>
  Phone Repair
</div>
<div class="service-card" style="left:319px">
  <svg viewBox="0 0 44 44" fill="none" stroke="#f7941d" stroke-width="2"><rect x="3" y="7" width="38" height="24" rx="1"/><line x1="3" y1="26" x2="41" y2="26"/><line x1="22" y1="31" x2="22" y2="37"/><line x1="14" y1="38" x2="30" y2="38"/></svg>
  TV Mounting
</div>
<div class="service-card" style="left:464px">
  <svg viewBox="0 0 44 44" fill="none" stroke="#f7941d" stroke-width="2"><rect x="4" y="8" width="36" height="6" rx="1"/><path d="M8 14 C8 28 36 28 36 14"/><circle cx="22" cy="22" r="4"/></svg>
  Security Camera<br>Installation
</div>
<div class="service-card" style="left:609px">
  <svg viewBox="0 0 44 44" fill="none" stroke="#f7941d" stroke-width="2.4" stroke-linecap="round"><path d="M4 18 a26 26 0 0 1 36 0"/><path d="M10 24 a17 17 0 0 1 24 0"/><path d="M16 30 a8 8 0 0 1 12 0"/><circle cx="22" cy="35" r="1.8" fill="#f7941d"/></svg>
  Networking /<br>Wi-Fi
</div>
<div class="service-card" style="left:754px">
  <svg viewBox="0 0 44 44" fill="none" stroke="#f7941d" stroke-width="2"><path d="M8 22 L22 10 L36 22"/><path d="M12 19 V38 H32 V19"/><path d="M19 26 h3 l4 -3 v10 l-4 -3 h-3 z"/><path d="M14 8 a12 12 0 0 1 16 0"/></svg>
  Smart Home<br>Services
</div>
<div class="service-card" style="left:898px">
  <svg viewBox="0 0 44 44" fill="none" stroke="#f7941d" stroke-width="2"><rect x="8" y="8" width="28" height="20" rx="1"/><path d="M3 32 H41 L38 36 H6 Z"/><circle cx="22" cy="18" r="5"/></svg>
  IT Support
</div>
<div class="btn offer-btn">BOOK SERVICES</div>

<!-- Call to action -->
<div class="abs cta-photo" role="img" aria-label="Photo of a smiling man using his phone in a bright kitchen with a woman in the background"></div>
<div class="abs cta-circle">
  <div class="cta-logo">Vanto Rim</div>
  <div class="cta-title">READY TO GET<br>STARTED?</div>
  <div class="cta-text">Repair or install<br>a device today.</div>
  <div class="btn cta-btn">BOOK SERVICES</div>
</div>

<!-- Testimonials -->
<h2 class="section-title centered testi-title">WHAT OUR CLIENT SAY</h2>
<div class="testi" style="left:161px">
  <div class="quote">&ldquo;</div>
  <p class="para">Lorem Ipsum is simply dummy text of the printing and typesetting industry. Lorem Ipsum has been the industry's standard dummy text ever since the 1500s, when an unknown printer took a galley.</p>
  <div class="person"><div class="avatar" role="img" aria-label="Client portrait"></div><div><div class="client-name">CLIENT NAME</div><div class="stars">★★★★★</div></div></div>
</div>
<div class="testi" style="left:466px">
  <div class="quote">&ldquo;</div>
  <p class="para">Lorem Ipsum is simply dummy text of the printing and typesetting industry. Lorem Ipsum has been the industry's standard dummy text ever since the 1500s, when an unknown printer took a galley.</p>
  <div class="person"><div class="avatar" role="img" aria-label="Client portrait"></div><div><div class="client-name">CLIENT NAME</div><div class="stars">★★★★★</div></div></div>
</div>
<div class="testi" style="left:769px">
  <div class="quote">&ldquo;</div>
  <p class="para">Lorem Ipsum is simply dummy text of the printing and typesetting industry. Lorem Ipsum has been the industry's standard dummy text ever since the 1500s, when an unknown printer took a galley.</p>
  <div class="person"><div class="avatar" role="img" aria-label="Client portrait"></div><div><div class="client-name">CLIENT NAME</div><div class="stars">★★★★★</div></div></div>
</div>

<!-- Pricing -->
<div class="abs pricing-bg"></div>
<h2 class="section-title centered pricing-title">PRICING</h2>
<div class="plan" style="left:285px;top:2651px;height:270px">
  <div class="price">$ 79 <small>/ year</small></div>
  <ul><li>Lorem Ipsum is simply</li><li>Lorem Ipsum is simply</li><li>Lorem Ipsum is simply</li><li>Lorem Ipsum is simply</li></ul>
  <div class="btn select">SELECT</div>
</div>
<div class="plan featured" style="left:501px;top:2631px;height:309px">
  <div class="price">$ 200 <small>/ year</small><span class="monthly">$ 20.75 / month</span></div>
  <ul><li>Lorem Ipsum is simply</li><li>Lorem Ipsum is simply</li><li>Lorem Ipsum is simply</li><li>Lorem Ipsum is simply</li><li>Lorem Ipsum is simply</li></ul>
  <div class="btn select">SELECT</div>
</div>
<div class="plan" style="left:719px;top:2651px;height:270px">
  <div class="price">$ 120 <small>/ year</small></div>
  <ul><li>Lorem Ipsum is simply</li><li>Lorem Ipsum is simply</li><li>Lorem Ipsum is simply</li><li>Lorem Ipsum is simply</li></ul>
  <div class="btn select">SELECT</div>
</div>

<!-- Areas served -->
<svg class="abs footer-wave" viewBox="0 0 1200 160" preserveAspectRatio="none" aria-hidden="true">
  <path d="M0 60 C 250 0, 520 10, 700 40 C 900 75, 1080 60, 1200 40 L1200 160 L0 160 Z" fill="#f7941d"/>
</svg>
<div class="abs areas-art" role="img" aria-label="Illustration of a man walking with a bag and phone beside a large phone screen showing a route map"></div>
<h2 class="section-title areas-title">AREAS SERVED</h2>

<div class="area-item" style="left:631px;top:3171px"><svg viewBox="0 0 14 18"><path d="M7 0a7 7 0 0 0-7 7c0 5 7 11 7 11s7-6 7-11a7 7 0 0 0-7-7z" fill="#f7941d"/><circle cx="7" cy="7" r="2.6" fill="#fff"/></svg>Lorem Ipsum is simply</div>
<div class="area-item" style="left:631px;top:3208px"><svg viewBox="0 0 14 18"><path d="M7 0a7 7 0 0 0-7 7c0 5 7 11 7 11s7-6 7-11a7 7 0 0 0-7-7z" fill="#f7941d"/><circle cx="7" cy="7" r="2.6" fill="#fff"/></svg>Lorem Ipsum is simply</div>
<div class="area-item" style="left:631px;top:3246px"><svg viewBox="0 0 14 18"><path d="M7 0a7 7 0 0 0-7 7c0 5 7 11 7 11s7-6 7-11a7 7 0 0 0-7-7z" fill="#f7941d"/><circle cx="7" cy="7" r="2.6" fill="#fff"/></svg>Lorem Ipsum is simply</div>
<div class="area-item" style="left:631px;top:3283px"><svg viewBox="0 0 14 18"><path d="M7 0a7 7 0 0 0-7 7c0 5 7 11 7 11s7-6 7-11a7 7 0 0 0-7-7z" fill="#f7941d"/><circle cx="7" cy="7" r="2.6" fill="#fff"/></svg>Lorem Ipsum is simply</div>
<div class="area-item" style="left:826px;top:3171px"><svg viewBox="0 0 14 18"><path d="M7 0a7 7 0 0 0-7 7c0 5 7 11 7 11s7-6 7-11a7 7 0 0 0-7-7z" fill="#f7941d"/><circle cx="7" cy="7" r="2.6" fill="#fff"/></svg>Lorem Ipsum is simply</div>
<div class="area-item" style="left:826px;top:3208px"><svg viewBox="0 0 14 18"><path d="M7 0a7 7 0 0 0-7 7c0 5 7 11 7 11s7-6 7-11a7 7 0 0 0-7-7z" fill="#f7941d"/><circle cx="7" cy="7" r="2.6" fill="#fff"/></svg>Lorem Ipsum is simply</div>
<div class="area-item" style="left:826px;top:3246px"><svg viewBox="0 0 14 18"><path d="M7 0a7 7 0 0 0-7 7c0 5 7 11 7 11s7-6 7-11a7 7 0 0 0-7-7z" fill="#f7941d"/><circle cx="7" cy="7" r="2.6" fill="#fff"/></svg>Lorem Ipsum is simply</div>
<div class="area-item" style="left:826px;top:3283px"><svg viewBox="0 0 14 18"><path d="M7 0a7 7 0 0 0-7 7c0 5 7 11 7 11s7-6 7-11a7 7 0 0 0-7-7z" fill="#f7941d"/><circle cx="7" cy="7" r="2.6" fill="#fff"/></svg>Lorem Ipsum is simply</div>

<div class="abs family-photo" role="img" aria-label="Photo of a happy family sitting together on a sofa looking at a phone"></div>

<!-- Footer -->
<footer class="abs footer"></footer>
<div class="abs footer-logo">Vanto Rim</div>
<div class="abs contact-box">
  <div class="contact-col">
    <div class="contact-icon"><svg width="18" height="24" viewBox="0 0 14 18" fill="none" stroke="#fff" stroke-width="1.2"><path d="M7 1a6 6 0 0 0-6 6c0 4.5 6 10 6 10s6-5.5 6-10a6 6 0 0 0-6-6z"/><circle cx="7" cy="7" r="2.2"/></svg></div>
    <div><div class="contact-label">Address</div><div class="contact-value">Lorem Ipsum is simply dummy<br>text of the printing</div></div>
  </div>
  <div class="contact-col">
    <div class="contact-icon"><svg width="22" height="22" viewBox="0 0 24 24" fill="none" stroke="#fff" stroke-width="1.4"><path d="M6.6 10.8a15 15 0 0 0 6.6 6.6l2.2-2.2c.3-.3.7-.4 1-.2 1.1.4 2.3.6 3.6.6.6 0 1 .4 1 1V20c0 .6-.4 1-1 1A17 17 0 0 1 3 4c0-.6.4-1 1-1h3.5c.6 0 1 .4 1 1 0 1.3.2 2.5.6 3.6.1.3 0 .7-.2 1z"/></svg></div>
    <div><div class="contact-label">Phone</div><div class="contact-value">123 456 7890</div></div>
  </div>
  <div class="contact-col">
    <div class="contact-icon"><svg width="24" height="18" viewBox="0 0 24 18" fill="none" stroke="#fff" stroke-width="1.4"><rect x="1" y="1" width="22" height="16" rx="1"/><path d="M1 2 L12 10 L23 2"/></svg></div>
    <div><div class="contact-label">Email</div><div class="contact-value">info@vantorim.com</div></div>
  </div>
</div>
<nav class="abs footer-links"><span>Home</span><span>About Us</span><span>Services</span><span>Pricing</span><span>Areas Served</span><span>Contact</span></nav>
<div class="abs copyright">© VANTO RIM - 2020. All Rights Reserved.</div>

</body>
</html>
```